Web Site for Strategy and Technology Consulting Company

We are looking for a website design that engages potential customers to understand our services and contact us. In this contest, we are looking for a homepage design, but the winning designer will be favored for the design of some of the more complicated interior pages of the site. An additional contest (or contests) for these pages will be added soon.

PLATROM AND RESPONSIVE DESIGN
The site will be implemented in WordPress using the Elementor page builder.
We are looking for a design that will look good on phones are well as laptop browsers.

UPLOADED FILES INCLUDE:
1a A wireframe of the homepage we are looking for. The Uploaded PDF also includes a draft of the text proposed for the homepage. Designers are free to go beyond the wireframe, but all elements of the wireframe should be included.
1b A Word document with the draft text of the homepage.
2a-d The Norvalith logo. Two versions are included – a dark version which works well against a light background, and a light version which works well against a dark background.
3 The Norvalith color palette with HEX and RGB values. Designers are not limited to this palette, but colors should be complementary.
4 A draft of the homepage menu
5 Service sheets with information on the services we provide

MORE ABOUT NORVALITH
Norvalith is a consulting company focused on transforming businesses through software. Our tagline, “Transformation Delivered,” recognizes the gap business often have between business transformation and the software they end up with. By listening to our customers and understanding their vision and where they are, we help get our customers where they want to go.

We increase our capability by working with many consultants and partners, allowing us to provide our customers with the best people and the software that best suits them.

Industry/Entity Type

Consulting

Number of Pages Required

1 page

Font styles to use
Sans Serif

Requirements
Must have
• the content represented on the wireframe uploaded
Nice to have
• interactive features, such as roll-over icons that reveal additional information

```html
<!DOCTYPE html>
<html lang="en">
<head>
<meta charset="utf-8">
<title>Norvalith – Transformation Delivered</title>
<link href="https://fonts.googleapis.com/css2?family=Poppins:wght@400;500;600&display=swap" rel="stylesheet">
<style>
:root{
  --navy:#24609a;
  --navy-deep:#153e66;
  --sky:#5ba3dc;
  --sky-pale:#bddbf0;
  --slate:#45556c;
  --slate-btn:#46566d;
  --yellow:#f3c623;
  --ink:#1b1b1b;
  --white:#ffffff;
  --line:#e3e7ec;
}
*{box-sizing:border-box;margin:0;padding:0}
html,body{width:1200px;height:2849px;overflow:hidden}
body{position:relative;font-family:'Poppins',sans-serif;color:var(--ink);background:var(--white)}
.abs{position:absolute}

/* header */
.site-header{left:0;top:0;width:1200px;height:60px;background:var(--white)}
.brand{left:125px;top:10px;font-size:32px;font-weight:500;color:var(--slate);letter-spacing:-0.5px}
.main-nav{left:420px;top:22px;display:flex;font-size:11px;font-weight:500}
.main-nav span{padding:0 16px;border-left:1px solid #333;line-height:24px}
.main-nav span:first-child{border-left:none;padding-left:0}
.btn-contact{left:957px;top:13px;width:117px;height:32px;border-radius:7px;background:var(--yellow);font-size:11px;font-weight:500;display:flex;align-items:center;justify-content:center}

/* hero */
.hero{left:0;top:60px;width:1200px;height:536px;background:var(--sky)}
.hero-photo{left:0;top:0;width:1200px;height:390px;background:linear-gradient(180deg,#b9cfe2 0%,#9dbfde 55%,var(--sky) 100%)}
.hero-title{left:0;top:302px;width:1200px;text-align:center;color:var(--white);font-size:40px;font-weight:600}
.hero-text{left:240px;top:368px;width:720px;text-align:center;color:var(--white);font-size:13.5px;line-height:20px}
.value-card{top:520px;width:200px;height:152px;background:var(--white);border:1px solid var(--line);border-radius:8px;box-shadow:0 12px 30px rgba(0,0,0,.08);text-align:center;font-size:11.5px;line-height:14px;padding:0 18px}
.value-card svg{display:block;margin:30px auto 16px}

/* how we work */
.kicker{left:0;top:778px;width:1200px;text-align:center;font-size:15px;font-weight:500}
.section-title{width:1200px;left:0;text-align:center;color:var(--navy);font-weight:600}
.how-title{top:795px;font-size:28px}
.how-text{left:255px;top:843px;width:690px;text-align:center;font-size:13.5px;line-height:17px}
.service-card{top:957px;width:182px;height:225px;background:var(--white);border:1px solid var(--line);border-radius:8px;text-align:center;overflow:visible}
.service-card .icon{position:absolute;left:53px;top:-25px;width:76px;height:76px;border-radius:50%;background:#dcdde0;display:flex;align-items:center;justify-content:center}
.service-card h3{position:absolute;top:71px;left:8px;right:8px;font-size:13px;font-weight:600;line-height:17px}
.service-card p{position:absolute;top:113px;left:22px;right:22px;font-size:11.5px;line-height:14px}
.service-card .learn{position:absolute;left:0;bottom:0;width:100%;height:36px;background:var(--slate-btn);color:var(--white);font-size:12.5px;font-weight:500;display:flex;align-items:center;justify-content:center;border-radius:0 0 8px 8px}
.service-card.active{background:var(--navy);color:var(--white);border-color:var(--navy);box-shadow:0 20px 40px rgba(0,0,0,.12)}
.service-card.active .learn{background:var(--yellow);color:var(--ink)}

/* people */
.people{left:0;top:1339px;width:1200px;height:480px;background:var(--slate)}
.people-photo{left:125px;top:1293px;width:382px;height:479px;border:3px solid var(--white);background:linear-gradient(135deg,#e9ecef 0%,#b9c8d7 55%,#6f8299 100%)}
.people-copy{left:587px;top:1400px;width:450px;color:var(--white)}
.people-copy h2{font-size:26px;font-weight:500;margin-bottom:18px}
.people-copy p{font-size:13px;line-height:16.5px}
.perk{display:flex;align-items:center;gap:14px;margin-top:28px;font-size:13px;line-height:16.5px}
.perk .badge{flex:none;width:36px;height:40px;border-radius:50%}
.people-close{margin-top:40px}

/* testimonial */
.testimonial{left:0;top:1819px;width:1200px;height:456px;background:var(--sky-pale)}
.t-title{top:1885px;font-size:30px}
.stars{left:568px;top:1934px}
.quote{left:300px;top:1984px;width:630px;text-align:center;font-size:16.5px;line-height:23.5px}
.avatar{left:521px;top:2101px;width:63px;height:63px;border-radius:50%;border:3px solid var(--yellow);background:linear-gradient(180deg,#c9a98e,#6b4a3b)}
.person{left:597px;top:2108px;font-size:14.5px;font-weight:600}
.person small{display:block;font-size:13px;font-weight:400;margin-top:2px}
.dots{display:flex;gap:9px}
.dots i{width:7px;height:7px;border-radius:50%;background:#333}
.dots i:first-child{background:#1f7cc6}

/* technologies */
.tech-title{top:2373px;font-size:30px}
.partner{top:2449px;height:40px;font-size:26px;line-height:40px;font-weight:500;text-align:center;white-space:nowrap}

/* footer */
.footer{left:0;top:2632px;width:1200px;height:173px;background:var(--navy);color:var(--white)}
.footer-brand{left:133px;top:2698px;font-size:36px;font-weight:500;color:var(--white)}
.contact-list{left:370px;top:2688px;font-size:11.5px;line-height:14px;color:var(--white)}
.contact-list div{display:flex;gap:8px;margin-bottom:10px}
.footer-links{left:656px;top:2686px;font-size:12.5px;line-height:24px;color:var(--white)}
.social{left:957px;top:2686px;display:flex;gap:13px}
.social i{width:18px;height:18px;border-radius:50%;background:var(--white)}
.copyright{left:0;top:2805px;width:1200px;height:44px;background:var(--navy-deep);color:var(--white);font-size:11px;display:flex;align-items:center;justify-content:center}
</style>
</head>
<body>

<header class="abs site-header">
  <div class="abs brand">Norvalith</div>
  <nav class="abs main-nav">
    <span>ABOUT US ⌄</span><span>SERVICES ⌄</span><span>INSIGHTS ⌄</span><span>JOIN US</span>
  </nav>
  <div class="abs btn-contact">CONTACT US</div>
</header>

<section class="abs hero">
  <div class="abs hero-photo" role="img" aria-label="Two smiling colleagues talking at an office desk"></div>
  <h1 class="abs hero-title">Transformation Delivered</h1>
  <p class="abs hero-text">We do more for our customers than implement software. We listen. We work to understand where they are in their transformation journey and where they want to go. We partner with them to clear the roadblocks that stand in their way, ensuring they reach their destination. At Norvalith, we:</p>
</section>

<div class="abs value-card" style="left:161px"><svg width="26" height="26" viewBox="0 0 26 26"><circle cx="13" cy="13" r="11.5" fill="none" stroke="#24609a" stroke-width="2"/><path d="M8 13.5l3.5 3.5 6.5-7" fill="none" stroke="#24609a" stroke-width="2"/></svg>Focus on business value, with an emphasis on delivering value quickly</div>
<div class="abs value-card" style="left:387px"><svg width="26" height="26" viewBox="0 0 26 26" style="margin-top:34px;margin-bottom:14px"><circle cx="13" cy="13" r="11.5" fill="none" stroke="#24609a" stroke-width="2"/><path d="M8 13.5l3.5 3.5 6.5-7" fill="none" stroke="#24609a" stroke-width="2"/></svg>Meet our customers where they are without backing them up to the beginning of their journey.</div>
<div class="abs value-card" style="left:613px"><svg width="26" height="26" viewBox="0 0 26 26" style="margin-top:34px"><circle cx="13" cy="13" r="11.5" fill="none" stroke="#24609a" stroke-width="2"/><path d="M8 13.5l3.5 3.5 6.5-7" fill="none" stroke="#24609a" stroke-width="2"/></svg>Provide a wide range of services, from strategy to product support.</div>
<div class="abs value-card" style="left:839px"><svg width="26" height="26" viewBox="0 0 26 26" style="margin-top:38px;margin-bottom:20px"><circle cx="13" cy="13" r="11.5" fill="none" stroke="#24609a" stroke-width="2"/><path d="M8 13.5l3.5 3.5 6.5-7" fill="none" stroke="#24609a" stroke-width="2"/></svg>Commit to our customer's long-term success.</div>

<div class="abs kicker">HOW WE WORK</div>
<h2 class="abs section-title how-title">Transformation Delivered</h2>
<p class="abs how-text">During our early years, Norvalith focused only on business transformation. We came to realize that successful transformation often depended on quality software implementations, and oftenmore than one. Now we focus on five things, the five things most businesses need to reach their goals.</p>

<article class="abs service-card active" style="left:125px">
  <div class="icon" role="img" aria-label="Strategy document icon"><svg width="40" height="40"><rect x="6" y="4" width="28" height="32" rx="2" fill="#fff"/><rect x="11" y="12" width="4" height="10" fill="#e24c4c"/><rect x="17" y="9" width="4" height="13" fill="#f3c623"/><rect x="22" y="20" width="12" height="14" fill="#4a8fe0"/></svg></div>
  <h3>Business<br>Transformation</h3>
  <p>Define and execute your strategy.</p>
  <div class="learn">LEARN MORE</div>
</article>
<article class="abs service-card" style="left:316px">
  <div class="icon" role="img" aria-label="ERP gear icon"><svg width="44" height="44"><circle cx="22" cy="22" r="13" fill="#1f7cc6"/><circle cx="22" cy="22" r="6" fill="#dcdde0"/></svg></div>
  <h3>ERP<br>Implementations</h3>
  <p style="top:115px">Assess, upgrade, and implement ERP solutions to meet your needs.</p>
  <div class="learn">LEARN MORE</div>
</article>
<article class="abs service-card" style="left:510px">
  <div class="icon" role="img" aria-label="Customer relationship icon"><svg width="44" height="44"><rect x="8" y="8" width="28" height="22" rx="3" fill="#2f7fd0"/><circle cx="15" cy="34" r="4" fill="#e24c4c"/><circle cx="29" cy="34" r="4" fill="#f3c623"/></svg></div>
  <h3>CRM<br>Implementation</h3>
  <p>Take your relationships to the next level.</p>
  <div class="learn">LEARN MORE</div>
</article>
<article class="abs service-card" style="left:702px">
  <div class="icon" role="img" aria-label="Database icon"><svg width="44" height="44"><ellipse cx="22" cy="10" rx="13" ry="5" fill="#5b6a82"/><rect x="9" y="10" width="26" height="22" fill="#45556c"/><ellipse cx="22" cy="32" rx="13" ry="5" fill="#45556c"/><circle cx="33" cy="33" r="7" fill="#2bb38a"/></svg></div>
  <h3 style="top:82px">BI and Data</h3>
  <p>Discover, connect, and trust your data</p>
  <div class="learn">LEARN MORE</div>
</article>
<article class="abs service-card" style="left:896px">
  <div class="icon" role="img" aria-label="Team of people icon"><svg width="44" height="44"><circle cx="22" cy="22" r="16" fill="#e24c4c"/><circle cx="22" cy="8" r="5" fill="#f3c623"/></svg></div>
  <h3>Building the Right<br>Team of People</h3>
  <p>Hire resources for your transformation journey.</p>
  <div class="learn">LEARN MORE</div>
</article>

<section class="abs people"></section>
<div class="abs people-photo" role="img" aria-label="Smiling consultant in glasses explaining a plan to a client at a desk"></div>
<div class="abs people-copy">
  <h2>It's the People</h2>
  <p>The world has changed in the past twenty years. The people you need might not all work for one company. Our clients want the best resources, available quickly. That's why, in addition to our team of experts, we partner with:</p>
  <div class="perk"><span class="badge" style="background:#f3b023" role="img" aria-label="Award ribbon icon"></span>A large network of expert consultants who are the best at what they do,</div>
  <div class="perk" style="margin-top:36px"><span class="badge" style="background:#8fb9e6" role="img" aria-label="Support agent icon"></span>Service providers all over the world to provide the resources and value that are right for you, available 24 x 7.</div>
  <p class="people-close">People are invariably at the center of our customer's success. Find out how we can add our experts to yours.</p>
</div>

<section class="abs testimonial"></section>
<h2 class="abs section-title t-title">Testimonial</h2>
<svg class="abs stars" width="115" height="20" viewBox="0 0 115 20">
  <g fill="#f3c623">
    <path id="star" d="M10 1l2.6 6 6.4.5-4.9 4.2 1.5 6.3L10 14.6 4.4 18l1.5-6.3L1 7.5l6.4-.5z"/>
    <use href="#star" x="24"/><use href="#star" x="48"/><use href="#star" x="72"/><use href="#star" x="96"/>
  </g>
</svg>
<p class="abs quote">“Meridian ERP from Calloway has totally changed the way we do business. Nunc et tortor vel elit condimentum tincidunt quis nec quam. Proin elementum nisl sed feugiat molestie. Nulla in ipsum sit amet tortor imperdiet lobortis id mattis arcu. In hac habitasse platea dictumst.”</p>
<svg class="abs" style="left:121px;top:2078px" width="22" height="20"><path d="M20 10H3M10 3L3 10l7 7" fill="none" stroke="#222" stroke-width="1.8"/></svg>
<svg class="abs" style="left:1052px;top:2078px" width="22" height="20"><path d="M2 10h17M12 3l7 7-7 7" fill="none" stroke="#222" stroke-width="1.8"/></svg>
<div class="abs avatar" role="img" aria-label="Portrait of the client"></div>
<div class="abs person">Lena Ortiz<small>CEO, Company</small></div>
<div class="abs dots" style="left:579px;top:2218px"><i></i><i></i><i></i></div>

<h2 class="abs section-title tech-title">Technologies</h2>
<svg class="abs" style="left:121px;top:2460px" width="22" height="20"><path d="M20 10H3M10 3L3 10l7 7" fill="none" stroke="#222" stroke-width="1.8"/></svg>
<svg class="abs" style="left:1043px;top:2460px" width="22" height="20"><path d="M2 10h17M12 3l7 7-7 7" fill="none" stroke="#222" stroke-width="1.8"/></svg>
<div class="abs partner" style="left:195px;width:135px;color:#4a7fd6">Quantora</div>
<div class="abs partner" style="left:350px;width:128px;color:#e8591a">Flowlink</div>
<div class="abs partner" style="left:505px;width:137px;color:#5a3f8c">Gridkit</div>
<div class="abs partner" style="left:830px;width:150px;color:#1b1b1b">Salesloom</div>
<div class="abs dots" style="left:579px;top:2511px"><i></i><i></i><i></i></div>

<footer class="abs footer"></footer>
<div class="abs footer-brand">Norvalith</div>
<div class="abs contact-list">
  <div><svg width="12" height="14"><path d="M6 13S1 8 1 5a5 5 0 0110 0c0 3-5 8-5 8z" fill="none" stroke="#7cd39b" stroke-width="1.3"/><circle cx="6" cy="5" r="1.8" fill="#7cd39b"/></svg><span>48 Harlow Creek Road<br>Eastfield, PA 17000</span></div>
  <div><svg width="12" height="12"><path d="M2 1l3 1 1 3-2 1.5a8 8 0 003.5 3.5L9 8l3 1v2.5C6 12 0 6 1 1z" fill="none" stroke="#7cd39b" stroke-width="1.2"/></svg><span>555-010-0142</span></div>
  <div><svg width="12" height="10"><rect x="0.6" y="0.6" width="10.8" height="8.8" fill="none" stroke="#7cd39b" stroke-width="1.2"/><path d="M1 1l5 4 5-4" fill="none" stroke="#7cd39b" stroke-width="1.2"/></svg><span>sales@norvalith-mail.com</span></div>
</div>
<div class="abs footer-links">About Us<br>Contact Us<br>Support</div>
<div class="abs social" aria-label="Social links"><i></i><i></i><i></i><i></i></div>
<div class="abs copyright">Copyright © 2023 Norvalith</div>

</body>
</html>
```